Awesome Dessert Baker needs Sticker Design

My wife is an incredible baker. She specializes in desserts and everyone that tastes her baked goods has told her to start selling them. She recently decided to go into business and just through word of mouth and her reputation she is already getting steady orders.

She is looking to have a sticker developed to put on her cake boxes and packaging.

She wants the following:
1. Colors to be used- hot pink, purple, white
2. Want a sleek, modern design and style incorporating following:
name: Whisked by Nola
tel: 917 382 6140
email: nola@whiskedbynola.example

**no old fashion baking references like rolling pins, aprons, ect.

We want the sticker to be very appealing and eye catching that will further promote her image and business.

Industry/Entity Type

Fashion

Requirements
Must have
• Must contain the following information:

Whisked by Nola
917 382 6140 (please make small and discreet)
nola@whiskedbynola.example (please make small and discreet)
Should not have
• **no old fashion baking references like rolling pins, aprons, ect.

```html
<!DOCTYPE html>
<html lang="en">
<head>
<meta charset="utf-8">
<title>Whisked by Nola – Sticker Options</title>
<link rel="stylesheet" href="https://fonts.googleapis.com/css2?family=Lilita+One&family=Open+Sans:ital,wght@1,700&display=swap">
<style>
  :root {
    --backdrop-centre: #ffffff;
    --backdrop-edge: #e9e9e9;
    --pink-deep: #c8157f;
    --pink-hot: #e6339a;
    --pink-light: #f06bb6;
    --purple-deep: #3e1f63;
    --purple-mid: #5b2f86;
    --purple-light: #7d4aa8;
    --cake-pink: #f29ab8;
    --white: #ffffff;
    --lemon: #fff200;
  }
  html, body {
    margin: 0;
    width: 1200px;
    height: 849px;
    overflow: hidden;
  }
  body {
    background: radial-gradient(ellipse at 50% 45%, var(--backdrop-centre) 0%, var(--backdrop-edge) 100%);
    position: relative;
  }
  .sticker {
    position: absolute;
    width: 312px;
    height: 276px;
  }
  .sticker--pink { left: 224px; top: 248px; }
  .sticker--purple { left: 688px; top: 239px; }
  .sticker svg { display: block; width: 100%; height: 100%; }
  .brand-name {
    font-family: "Lilita One", "Arial Black", sans-serif;
    font-size: 40px;
  }
  .contact {
    font-family: "Open Sans", Arial, sans-serif;
    font-style: italic;
    font-weight: 700;
    fill: var(--white);
  }
  .contact--phone { font-size: 16px; }
  .contact--email { font-size: 12px; }
</style>
</head>
<body>

  <div class="sticker sticker--pink">
    <svg viewBox="0 0 312 276" xmlns="http://www.w3.org/2000/svg">
      <defs>
        <radialGradient id="burst-pink" cx="0.35" cy="0.45" r="0.8">
          <stop offset="0" stop-color="var(--pink-light)"/>
          <stop offset="1" stop-color="var(--pink-hot)"/>
        </radialGradient>
      </defs>
      <path class="sticker-edge" d="M0 276 V72 Q0 0 72 0 H312 V276 Z" fill="var(--pink-deep)"/>
      <path class="sticker-face" d="M7 269 V74 Q7 7 74 7 H305 V269 Z" fill="url(#burst-pink)" stroke="var(--white)" stroke-width="3"/>
      <circle class="brand-mark" cx="72" cy="150" r="50" fill="var(--cake-pink)"/>
      <text class="brand-name" x="132" y="128" fill="var(--white)">Whisked</text>
      <text class="brand-name" x="132" y="174" fill="var(--white)">by Nola</text>
      <text class="contact contact--phone" x="290" y="236" text-anchor="end">917 382 6140</text>
      <text class="contact contact--email" x="290" y="252" text-anchor="end">nola@whiskedbynola.example</text>
    </svg>
  </div>

  <div class="sticker sticker--purple">
    <svg viewBox="0 0 312 276" xmlns="http://www.w3.org/2000/svg">
      <defs>
        <radialGradient id="burst-purple" cx="0.35" cy="0.45" r="0.8">
          <stop offset="0" stop-color="var(--purple-light)"/>
          <stop offset="1" stop-color="var(--purple-deep)"/>
        </radialGradient>
      </defs>
      <path class="sticker-edge" d="M0 276 V72 Q0 0 72 0 H312 V276 Z" fill="var(--purple-deep)"/>
      <path class="sticker-face" d="M7 269 V74 Q7 7 74 7 H305 V269 Z" fill="url(#burst-purple)" stroke="var(--white)" stroke-width="3"/>
      <circle class="brand-mark" cx="72" cy="150" r="50" fill="var(--cake-pink)"/>
      <text class="brand-name" x="132" y="128" fill="var(--lemon)">Whisked</text>
      <text class="brand-name" x="132" y="174" fill="var(--lemon)">by Nola</text>
      <text class="contact contact--phone" x="290" y="236" text-anchor="end">917 382 6140</text>
      <text class="contact contact--email" x="290" y="252" text-anchor="end">nola@whiskedbynola.example</text>
    </svg>
  </div>

</body>
</html>
```